Social media post for the holidays

Create 2 social media post. 1 for Christmas & 1 for New Years.
See attached logo, try to copy our house style.
a sleek clean design.

After we except the design in EPS from so we can add/change text.
https://www.facebook.com/Haulpoint41

```html
<!DOCTYPE html>
<html lang="en">
<head>
<meta charset="utf-8">
<title>Merry Christmas – Haulpoint41</title>
<link rel="stylesheet" href="https://fonts.googleapis.com/css2?family=Josefin+Sans:wght@600;700&display=swap">
<style>
  :root {
    --night: #1b2768;
    --night-deep: #16205a;
    --sky-top: #17236a;
    --glow-red: rgba(214, 52, 104, 0.75);
    --glow-amber: rgba(247, 170, 90, 0.7);
    --glow-pink: rgba(240, 110, 170, 0.65);
    --glow-blue: rgba(24, 120, 210, 0.75);
    --gold: rgba(255, 200, 130, 0.55);
    --spark: #ffd9a0;
    --headline: #ffffff;
    --brand: #ffffff;
    --line: #f4f1ea;
    --accent-red: #c8283c;
  }
  html, body {
    margin: 0;
    padding: 0;
    overflow: hidden;
    background: var(--night-deep);
  }
  .post {
    position: relative;
    width: 1200px;
    height: 1200px;
    overflow: hidden;
    background:
      radial-gradient(circle at 156px 667px, var(--glow-red) 0, transparent 120px),
      radial-gradient(circle at 422px 570px, var(--glow-amber) 0, transparent 170px),
      radial-gradient(circle at 322px 844px, var(--glow-pink) 0, transparent 140px),
      radial-gradient(circle at 789px 289px, var(--glow-blue) 0, transparent 200px),
      radial-gradient(circle at 911px 811px, var(--glow-blue) 0, transparent 200px),
      radial-gradient(ellipse at 300px 650px, rgba(120, 60, 150, 0.45) 0, transparent 420px),
      var(--night);
  }
  .falling-sparks {
    position: absolute;
    left: 0;
    top: 0;
    width: 1200px;
    height: 470px;
    background:
      linear-gradient(180deg, var(--sky-top) 0%, rgba(23, 35, 106, 0.85) 30%, rgba(23, 35, 106, 0) 100%),
      radial-gradient(ellipse 620px 220px at 600px 140px, var(--gold) 0, transparent 100%);
    -webkit-mask-image: linear-gradient(180deg, #000 70%, transparent 100%);
    mask-image: linear-gradient(180deg, #000 70%, transparent 100%);
  }
  .headline {
    position: absolute;
    left: 0;
    top: 482px;
    width: 1200px;
    margin: 0;
    text-align: center;
    font-family: "Josefin Sans", sans-serif;
    font-weight: 600;
    font-size: 114px;
    line-height: 136px;
    letter-spacing: 0;
    color: var(--headline);
    text-shadow: 0 0 18px rgba(255, 255, 255, 0.55), 0 0 4px rgba(255, 255, 255, 0.8);
  }
  .tree-lights {
    position: absolute;
    left: 88px;
    top: 975px;
    width: 126px;
    height: 210px;
    background: radial-gradient(ellipse 60px 105px at 50% 50%, rgba(255, 236, 200, 0.28) 0, rgba(255, 217, 160, 0.08) 70%, transparent 100%);
  }
  .ground-line {
    position: absolute;
    left: 0;
    top: 1140px;
    width: 1200px;
    height: 40px;
  }
  .brand {
    position: absolute;
    right: 42px;
    top: 1098px;
    display: flex;
    align-items: center;
    gap: 10px;
    font-family: "Josefin Sans", sans-serif;
    font-weight: 700;
    font-size: 40px;
    line-height: 1;
    color: var(--brand);
  }
  .brand-mark {
    width: 16px;
    height: 16px;
    background: var(--brand);
  }
</style>
</head>
<body>
  <main class="post">
    <div class="falling-sparks" role="img" aria-label="Curtain of golden falling star streaks on a starry night sky"></div>

    <h1 class="headline">MERRY<br>CHRISTMAS</h1>

    <div class="tree-lights" role="img" aria-label="Line-drawn Christmas tree with small glowing lights"></div>

    <svg class="ground-line" viewBox="0 0 1200 40" aria-hidden="true">
      <path d="M214 22 L960 22" fill="none" stroke="var(--line)" stroke-width="2"/>
      <path d="M960 22 L1080 22" fill="none" stroke="var(--accent-red)" stroke-width="3"/>
      <g fill="var(--spark)">
        <circle cx="415" cy="22" r="3"/>
        <circle cx="643" cy="22" r="3"/>
        <circle cx="968" cy="22" r="3"/>
      </g>
    </svg>

    <div class="brand">
      <span class="brand-mark" aria-hidden="true"></span>
      <span class="brand-name">Haulpoint41</span>
    </div>
  </main>
</body>
</html>
```